依頼詳細
このたびは、「緑茶ハイ・緑茶」専用メニュー表(A4片面)のデザインを募集いたします。

【メニュー表に入れていただきたい要素】
・ロゴ「凪色 Harbor」を、おしゃれなレトロ調で作成。メニュー表の上端にロゴを入れる。
・ユーモアで面白さもありつつ、少し高級感もあるデザイン。
・シリーズ化できる(これから緑茶以外にも紅茶ハイなども展開する可能性があります)
・「飲むならこの緑茶ハイがいいな!」と思われるようなデザインやキャッチコピー。
・飲食店の他メニュー表と一緒に置いていて、目を引くデザイン。

【コンペの流れ】
①ご応募ください。
②作成したデザインをご提出ください。
③コンペ終了後、採用者の選定をさせていただきます。

【デザイン提出方法】
PDFデータまたは、AIデータをお送りください。
※採用させていただいた場合、最終納品はイラストレーター形式(.ai)にてお願いします。

【備考】
ご提案いただいたデザインの編集依頼をすることがございます。
納期まで余裕をもってご提案頂けますと幸いです。
納期を過ぎてのご提案は受け付けておりませんので、予めご了承ください。
注意点】
コンペで採用となった場合、著作権は弊社に帰属します。

【継続依頼について】
スキル、センス、クオリティの高さなどにより、継続的な依頼を検討いたします。
記載項目
【メニュー表に入れていただきたい内容】
・緑茶ハイと緑茶の写真画像(デザイナー様の選定でお願いします)
・「緑茶ハイと緑茶」の値段が入れられる場所
(金額は仮で¥500と記載をお願いします)
・とっても美味しい静岡県産掛川市の茶葉を使用。
・無添加、無農薬のお茶粉。
・お茶粉のスティック写真を盛り込む(添付画像データをお使いください)。
※商品チラシデータを添付しています。
栄養や安全性、美味しさの詳細が書かれていますのでご覧ください。
サイズ
A4
ページ数
片面
希望イメージ
シンプル 複雑
単色 カラフル
暗い 明るい
日常 高級
遊び心 厳粛
未来的 伝統的
女性的 男性的
希望する色
緑系
納品ファイル
• イラストレーター形式 (.ai)
〆切を4/5に延長させていただきました!
どうか、デザイナーの方々のお力を貸してください!
よろしくお願いいたします。
みなさまのご協力をお待ちしております。
よろしくお願いいたします!
■ 選んだ理由

弊社のイメージするデザインに1番近かったため。

■ 提案者全員のお礼・コメント

素敵なデザインを作成していただき、ありがとうございます!

```html
<!DOCTYPE html>
<html lang="ja">
<head>
<meta charset="utf-8">
<title>緑茶ハイ・緑茶 メニュー</title>
<link href="https://fonts.googleapis.com/css2?family=Noto+Sans+JP:wght@500;700;900&family=Noto+Serif+JP:wght@700;900&display=swap" rel="stylesheet">
<style>
  :root {
    --green-deep: #0f5a1e;
    --green: #1f8a2c;
    --green-light: #4cb03a;
    --tea: #7fb51c;
    --gold: #c9a441;
    --gold-light: #f2dc8a;
    --cream: #fffbe6;
    --white: #ffffff;
    --ink: #1c2a12;
  }
  * { margin: 0; padding: 0; box-sizing: border-box; }
  html, body { width: 846px; height: 1200px; overflow: hidden; }
  body { font-family: "Noto Sans JP", sans-serif; background: #fff; }
  .menu {
    position: relative; width: 846px; height: 1200px; overflow: hidden;
    background: linear-gradient(160deg, #d9a36a 0%, #c24a2a 30%, #6f8d2a 55%, #3f6a1c 80%, #2f5a16 100%);
  }
  .menu__backdrop { position: absolute; inset: 0; }
  .brand-badge {
    position: absolute; left: 20px; top: 20px; width: 170px; height: 170px; border-radius: 50%;
    background: radial-gradient(circle at 40% 35%, var(--gold-light), var(--gold) 60%, #8a6a1e);
    border: 4px solid #fff6d0;
    display: flex; flex-direction: column; align-items: center; justify-content: center;
    color: var(--white); font-family: "Noto Serif JP", serif; font-weight: 900;
  }
  .brand-badge__jp { font-size: 50px; line-height: 1; }
  .brand-badge__en { font-size: 26px; line-height: 1.3; }
  .headline {
    position: absolute; writing-mode: vertical-rl; font-weight: 900; line-height: 1;
  }
  .headline--lead {
    right: 44px; top: 26px; font-size: 60px; color: var(--white); letter-spacing: 0.02em;
    text-shadow: 0 2px 6px rgba(0,0,0,.35);
  }
  .headline--lead span { display: block; margin-left: 18px; }
  .headline--product {
    left: 430px; top: 84px; font-size: 78px; color: var(--green);
    -webkit-text-stroke: 3px var(--white); paint-order: stroke fill;
    text-shadow: 0 3px 8px rgba(0,0,0,.3); letter-spacing: -0.02em;
  }
  .glass-photo {
    position: absolute; left: 98px; top: 210px; width: 240px; height: 470px;
    background: linear-gradient(180deg, #d7ec9a 0%, var(--tea) 35%, #4f8a12 100%);
    border-radius: 10px 10px 24px 24px;
  }
  .nutrients {
    position: absolute; left: 662px; top: 508px; width: 172px; padding: 8px 8px;
    background: rgba(15,90,30,.78); color: var(--white); font-size: 12.5px; line-height: 1.45; font-weight: 500;
  }
  .nutrients__note { margin-top: 6px; font-size: 9px; line-height: 1.35; }
  .catch {
    position: absolute; left: 268px; top: 712px; width: 400px; text-align: center;
    font-family: "Noto Serif JP", serif;
    color: var(--cream); font-weight: 900; font-size: 38px; line-height: 1.2; white-space: nowrap;
    -webkit-text-stroke: 6px var(--green-deep); paint-order: stroke fill;
  }
  .person-photo {
    position: absolute; left: 682px; top: 700px; width: 110px; height: 150px;
    background: linear-gradient(180deg, #eef3e6, #5e8c3a);
    border-radius: 4px;
  }
  .price-band {
    position: absolute; left: 0; right: 0; top: 850px; bottom: 0;
    background: linear-gradient(180deg, var(--green-light) 0%, var(--green) 35%, var(--green-deep) 100%);
  }
  .price-list {
    position: absolute; right: 40px; top: 880px; color: var(--white); font-weight: 900;
    font-family: "Noto Serif JP", serif;
  }
  .price-list__row { display: flex; justify-content: flex-end; gap: 26px; font-size: 52px; line-height: 1.3; }
  .stick-photo {
    position: absolute; left: 84px; top: 735px; width: 184px; height: 380px;
    background: linear-gradient(160deg, #f4d35a, #d8452c 55%, #7b2a1c);
    transform: rotate(-10deg);
  }
  .quality-badge { position: absolute; left: 60px; top: 1050px; width: 270px; height: 80px; }
  .quality-badge__text {
    position: absolute; left: 0; right: 0; bottom: 8px; text-align: center;
    color: var(--white); font-size: 17px; font-weight: 900;
  }
</style>
</head>
<body>
<main class="menu">
  <div class="menu__backdrop" role="img" aria-label="色とりどりの新鮮な野菜の写真"></div>

  <div class="brand-badge">
    <span class="brand-badge__jp">凪色</span>
    <span class="brand-badge__en">Harbor</span>
  </div>

  <h2 class="headline headline--lead"><span>この一杯に</span><span>30種の栄養素</span></h2>
  <h1 class="headline headline--product">緑茶ハイ・緑茶</h1>

  <div class="glass-photo" role="img" aria-label="グラスに注がれた緑茶ハイの写真"></div>

  <div class="nutrients">
    含まれる栄養素は、カテキン・食物繊維・ビタミンA・ビタミンB・ビタミンC・ビタミンE・カロテン・葉酸・カリウム・カルシウム・鉄・コエンザイムQ10他
    <p class="nutrients__note">毎日の一杯で、体にうれしい栄養をおいしく手軽に。</p>
  </div>

  <div class="price-band"></div>

  <div class="person-photo" role="img" aria-label="茶畑で茶摘みをする人の写真"></div>

  <p class="catch">とっても美味しい！<br>静岡県産掛川市の<br>茶葉を使用</p>

  <div class="price-list">
    <p class="price-list__row"><span>緑茶ハイ</span><span>¥500</span></p>
    <p class="price-list__row"><span>緑茶</span><span>¥500</span></p>
  </div>

  <div class="stick-photo" role="img" aria-label="お茶粉スティック商品の写真"></div>

  <div class="quality-badge">
    <svg width="270" height="80" viewBox="0 0 270 80" aria-hidden="true">
      <rect x="10" y="44" width="250" height="32" rx="4" fill="var(--green-deep)" stroke="var(--gold)" stroke-width="3"/>
    </svg>
    <p class="quality-badge__text">無添加 無農薬のお茶粉</p>
  </div>
</main>
</body>
</html>
```